Zarvo! Next Steps?, Bail Bond Company Check-in App , Court date, Court Reminders, Payments

Zarvo!
Next Steps?
WINNER OF THIS CONTEST WILL HAVE OPPORTUNITY TO DESIGN CUSTOMIZE SOME OUR COMPANY PAGES AFTER CONTEST!
Check-in with your Bail agent via pic/video
Receive Court reminders
Make a payments

Basically this app is a portal to 3rd party bail companies.
The idea is for the person whom makes bail downloads the Zarvo app from App Store.
Then they select a bail bond company.
This would be similar to a restaurant, real estate agent, insurance agent,,app where we could populate bail bond companies by client location or by typing in name of bail company.
We would like the ability to customize each bail bond company landing pages but are open to a global concept. when you click the bail bond company location it would have the logos for that company so the bail bond company screens would need to be customizeble
The app will require a photo or video check-in that is date and time
stamped with a gps location stored in check-in history
Check-in can be scheduled or random or voluntary
Voluntary and Scheduled Check-ins would require check-in button
Random would be via alert or text

The app should be able to receive court date updates
The app should allow clients to make payments to bail bond company
we need
ZARVO! landing page
client registration screens, check-in screens, available bail bond company screens for client to choose from
client registration page should include
name
email address
phone number
picture
home address
work address
date of birth
this app is different from our u-trak app. this is a bail bond check-in app for third party bail bond companies.
landing page should be ZARVO! Next Steps?
ZARVO ! Registration
Find your bail bond Company should list bail bond companies near me and search bar for searching bail bond companies by name
Next landing pages would be customizable for the third party bail bond companies
these would include pages for
check-ins via pics/videos
payment page
court reminders
contact information for bail bond companies
Zarvo Pages include
initial landing page
registration page
search bail companies

Bail bond company pages should include
Bali bond company landing page
Use KELNOR BAIL BOND COMPANY as example
contact information for bail company
check-in page
payment page
court reminder page
Updates

Low designer entries

Low designer entries

Sick

Sick

Sick

Target Market(s)

Court Defendants, Probation ,jails, sheriffs, judges, attorneys

Industry/Entity Type

justice, law enforcement, courts,

Requirements
Must have
• Check-in via pic/video, ability to receive court date reminders, make paymentswe need client registration screens, check-in screens, available bail bond company screens for client to choose from
Nice to have
• Professional easy to navigate intuitive customizable to 3rd party bail bond companies, logos,phone numbers etc.
Should not have
• unprofessional graphics,

```html
<!DOCTYPE html>
<html lang="en">
<head>
<meta charset="utf-8">
<title>Zarvo! Next Steps? – App Screens</title>
<link rel="stylesheet" href="https://fonts.googleapis.com/css2?family=Playfair+Display:wght@700;900&family=Poppins:wght@400;500;600;700&display=swap">
<style>
  :root{
    --bg:#1c1c1d;
    --panel-dark:#1f1f20;
    --white:#ffffff;
    --field:#efefef;
    --ink:#141414;
    --muted:#7a7a7a;
    --red:#c01e2d;
    --pink:#f6e4e6;
    --row:#f1f1f1;
    --tile-shadow:0 2px 8px rgba(0,0,0,.12);
  }
  *{box-sizing:border-box;margin:0;padding:0}
  html,body{width:1200px;height:2305px;overflow:hidden;background:var(--bg);font-family:'Poppins',sans-serif;color:var(--ink)}
  .screen{position:absolute;width:439px;height:952px;border-radius:56px;overflow:hidden;transform:scale(.895);transform-origin:0 0}
  .abs{position:absolute}
  .serif{font-family:'Playfair Display',serif;font-weight:900}

  /* Splash */
  .splash{left:160px;top:216px}
  .splash-photo{position:absolute;inset:0;background:
    linear-gradient(160deg,#2a2a2b 0%,#3b3b3c 30%,#1d1d1e 60%,#111 100%)}
  .splash-title{position:absolute;left:0;right:0;top:428px;text-align:center;color:var(--white);font-family:'Playfair Display',serif;font-weight:700;font-size:74px;line-height:1}
  .splash-sub{position:absolute;left:0;right:0;top:508px;text-align:center;color:var(--white);font-size:19.5px}

  /* Registration */
  .registration{left:647px;top:319px;background:var(--white)}
  .reg-title{left:0;right:0;top:78px;text-align:center;font-size:42px;line-height:1.1}
  .reg-sub{left:0;right:0;top:133px;text-align:center;font-size:14px;color:#444}
  .label{left:36px;font-size:9.5px;font-weight:600;letter-spacing:.2px}
  .field{left:36px;width:367px;height:42px;background:var(--field);border-radius:2px;font-size:10px;color:var(--muted);padding:14px 16px}
  .upload{left:36px;width:367px;height:150px;background:var(--field);border-radius:2px}
  .upload-inner{position:absolute;inset:10px;border:1px dashed #c2c2c2;border-radius:4px}
  .upload-badge{position:absolute;left:50%;top:50%;width:56px;height:56px;margin:-28px 0 0 -28px;border-radius:50%;background:var(--white);display:flex;align-items:center;justify-content:center}
  .cal-icon{position:absolute;right:16px;top:13px}
  .btn-red{background:var(--red);color:var(--white);font-weight:700;display:flex;align-items:center;justify-content:center;border-radius:2px}
  .submit{left:36px;top:810px;width:367px;height:52px;font-size:16px}
  .submit svg{position:absolute;right:18px;top:18px}

  /* Shared dark header */
  .app-screen{background:var(--panel-dark)}
  .app-head{left:0;right:0;top:62px;text-align:center;color:var(--white);font-size:33px}
  .back{left:34px;top:78px}
  .more{right:36px;top:78px}
  .sheet{left:0;right:0;bottom:0;background:var(--white);border-radius:32px 32px 0 0}

  /* Company */
  .company{left:160px;top:1118px}
  .company .sheet{top:141px}
  .section-head{left:35px;top:182px;font-size:15.5px;font-weight:600}
  .office-label{left:35px;font-size:15px;font-weight:600}
  .tile{width:114px;height:115px;border-radius:8px;background:var(--white);box-shadow:var(--tile-shadow);display:flex;flex-direction:column;align-items:center;justify-content:flex-start;padding-top:24px;font-size:12px;color:#333}
  .tile svg{margin-bottom:18px}
  .tile.active{background:var(--red);color:var(--white)}
  .call-bar{left:35px;top:847px;width:362px;height:52px;font-size:17px;position:absolute}
  .call-bar svg{position:absolute;left:20px;top:16px}

  /* Check-in */
  .checkin{left:647px;top:1237px}
  .checkin .sheet{top:140px}
  .cam{left:164px;top:202px}
  .cam-text{left:0;right:0;top:305px;text-align:center;font-size:18px;line-height:1.35;color:#222}
  .dates-head{left:35px;top:390px;font-size:19px;font-weight:600;letter-spacing:.3px}
  .court-row{left:20px;width:399px;height:75px}
  .court-row.shaded{background:var(--row)}
  .day{position:absolute;left:22px;top:14px;width:44px;text-align:center;color:var(--red);font-weight:700;font-size:30px;line-height:1}
  .dow{position:absolute;left:22px;top:45px;width:44px;text-align:center;color:var(--red);font-size:8.5px;font-weight:500}
  .court-name{position:absolute;left:77px;top:14px;font-size:16px;font-weight:600}
  .court-time{position:absolute;left:77px;top:38px;font-size:10.5px;color:#333}
  .fee{position:absolute;right:23px;top:22px;color:var(--red);font-weight:700;font-size:17px}
  .btn-cancel{left:30px;top:846px;width:133px;height:52px;background:var(--pink);color:#444;font-weight:600;font-size:16px;display:flex;align-items:center;justify-content:center;border-radius:2px}
  .btn-next{left:275px;top:846px;width:133px;height:52px;font-size:16px;position:absolute}
</style>
</head>
<body>

<!-- Landing -->
<section class="screen splash">
  <div class="splash-photo" role="img" aria-label="Dark moody photo of barred shadows falling across a floor"></div>
  <h1 class="splash-title">Zarvo</h1>
  <p class="splash-sub">Online Zarvo Management</p>
</section>

<!-- Registration -->
<section class="screen registration">
  <h2 class="abs serif reg-title">Registration</h2>
  <p class="abs reg-sub">Online Zarvo App</p>

  <span class="abs label" style="top:175px">NAME*</span>
  <div class="abs field" style="top:191px">Enter name</div>
  <span class="abs label" style="top:243px">EMAIL ADDRESS*</span>
  <div class="abs field" style="top:260px">Enter email address</div>
  <span class="abs label" style="top:314px">PHONE NUMBER*</span>
  <div class="abs field" style="top:330px">Enter phone number</div>
  <span class="abs label" style="top:385px">PICTURE*</span>
  <div class="abs upload" style="top:403px">
    <div class="upload-inner"></div>
    <div class="upload-badge">
      <svg width="22" height="20" viewBox="0 0 22 20" fill="none" stroke="#222" stroke-width="1.4"><rect x="1" y="2" width="17" height="15" rx="1.5"/><circle cx="6" cy="7" r="1.6"/><path d="M2 15l5-5 4 4 3-3 4 4"/><path d="M18 2v-1M18 1l-2 2M18 1l2 2" /></svg>
    </div>
  </div>
  <span class="abs label" style="top:572px">HOME ADDRESS*</span>
  <div class="abs field" style="top:588px">Enter home address</div>
  <span class="abs label" style="top:643px">WORK ADDRESS*</span>
  <div class="abs field" style="top:659px">Enter work address</div>
  <span class="abs label" style="top:713px">DATE OF BIRTH *</span>
  <div class="abs field" style="top:730px">Select date of birth
    <svg class="cal-icon" width="14" height="14" viewBox="0 0 14 14" fill="none" stroke="#555" stroke-width="1"><rect x="1" y="2" width="12" height="11"/><path d="M1 5h12M4 1v2M10 1v2M4 7h1M7 7h1M10 7h1M4 10h1M7 10h1M10 10h1"/></svg>
  </div>
  <div class="abs btn-red submit">SUBMIT
    <svg width="18" height="16" viewBox="0 0 18 16" fill="#fff"><path d="M17 1L1 8l5 2 1 5 3-3 4 3z"/></svg>
  </div>
</section>

<!-- Bail company contact -->
<section class="screen app-screen company">
  <svg class="abs back" width="14" height="22" viewBox="0 0 14 22" fill="none" stroke="#fff" stroke-width="2.6"><path d="M11 2L3 11l8 9"/></svg>
  <h2 class="abs serif app-head">Company name</h2>
  <svg class="abs more" width="6" height="22" viewBox="0 0 6 22" fill="#fff"><circle cx="3" cy="3" r="2.5"/><circle cx="3" cy="11" r="2.5"/><circle cx="3" cy="19" r="2.5"/></svg>
  <div class="abs sheet"></div>
  <h3 class="abs section-head">OFFICE LOCATIONS</h3>

  <!-- reusable icon sets via inline markup per office -->
  <span class="abs office-label" style="top:224px">Office 1</span>
  <div class="abs tile" style="left:35px;top:250px"><svg width="38" height="38" viewBox="0 0 38 38" fill="none" stroke="#222" stroke-width="1.4"><path d="M8 4l6 6-3 4c2 5 6 9 11 11l4-3 6 6-4 5C17 33 5 21 3 8z"/><path d="M21 6a11 11 0 0 1 11 11M21 2a15 15 0 0 1 15 15M21 10a7 7 0 0 1 7 7"/></svg>Call</div>
  <div class="abs tile" style="left:158px;top:250px"><svg width="38" height="38" viewBox="0 0 38 38" fill="none" stroke="#222" stroke-width="1.4"><path d="M19 37V10M19 2l-4 6h8z M19 20L9 12M6 9l2 5 3-3z M19 20l10-8M32 9l-5 2 3 3z M19 26L7 22M19 26l12-4"/></svg>Direction</div>
  <div class="abs tile" style="left:281px;top:250px"><svg width="40" height="38" viewBox="0 0 40 38" fill="none" stroke="#222" stroke-width="1.4"><path d="M20 24s-7-8-7-13a7 7 0 0 1 14 0c0 5-7 13-7 13z"/><circle cx="20" cy="11" r="2.6"/><path d="M12 20l-9 3-1 13 12-3 12 3 12-3-1-13-8-3"/><path d="M8 31l5-4 5 3 6-4" stroke-dasharray="2 2"/></svg>Map</div>

  <span class="abs office-label" style="top:374px">Office 2</span>
  <div class="abs tile active" style="left:35px;top:400px"><svg width="38" height="38" viewBox="0 0 38 38" fill="none" stroke="#fff" stroke-width="1.4"><path d="M8 4l6 6-3 4c2 5 6 9 11 11l4-3 6 6-4 5C17 33 5 21 3 8z"/><path d="M21 6a11 11 0 0 1 11 11M21 2a15 15 0 0 1 15 15M21 10a7 7 0 0 1 7 7"/></svg>Call</div>
  <div class="abs tile" style="left:158px;top:400px"><svg width="38" height="38" viewBox="0 0 38 38" fill="none" stroke="#222" stroke-width="1.4"><path d="M19 37V10M19 2l-4 6h8z M19 20L9 12M6 9l2 5 3-3z M19 20l10-8M32 9l-5 2 3 3z M19 26L7 22M19 26l12-4"/></svg>Direction</div>
  <div class="abs tile" style="left:281px;top:400px"><svg width="40" height="38" viewBox="0 0 40 38" fill="none" stroke="#222" stroke-width="1.4"><path d="M20 24s-7-8-7-13a7 7 0 0 1 14 0c0 5-7 13-7 13z"/><circle cx="20" cy="11" r="2.6"/><path d="M12 20l-9 3-1 13 12-3 12 3 12-3-1-13-8-3"/><path d="M8 31l5-4 5 3 6-4" stroke-dasharray="2 2"/></svg>Map</div>

  <span class="abs office-label" style="top:528px">Office 3</span>
  <div class="abs tile" style="left:35px;top:554px"><svg width="38" height="38" viewBox="0 0 38 38" fill="none" stroke="#222" stroke-width="1.4"><path d="M8 4l6 6-3 4c2 5 6 9 11 11l4-3 6 6-4 5C17 33 5 21 3 8z"/><path d="M21 6a11 11 0 0 1 11 11M21 2a15 15 0 0 1 15 15M21 10a7 7 0 0 1 7 7"/></svg>Call</div>
  <div class="abs tile" style="left:158px;top:554px"><svg width="38" height="38" viewBox="0 0 38 38" fill="none" stroke="#222" stroke-width="1.4"><path d="M19 37V10M19 2l-4 6h8z M19 20L9 12M6 9l2 5 3-3z M19 20l10-8M32 9l-5 2 3 3z M19 26L7 22M19 26l12-4"/></svg>Direction</div>
  <div class="abs tile" style="left:281px;top:554px"><svg width="40" height="38" viewBox="0 0 40 38" fill="none" stroke="#222" stroke-width="1.4"><path d="M20 24s-7-8-7-13a7 7 0 0 1 14 0c0 5-7 13-7 13z"/><circle cx="20" cy="11" r="2.6"/><path d="M12 20l-9 3-1 13 12-3 12 3 12-3-1-13-8-3"/><path d="M8 31l5-4 5 3 6-4" stroke-dasharray="2 2"/></svg>Map</div>

  <span class="abs office-label" style="top:678px">Office 4</span>
  <div class="abs tile" style="left:35px;top:704px"><svg width="38" height="38" viewBox="0 0 38 38" fill="none" stroke="#222" stroke-width="1.4"><path d="M8 4l6 6-3 4c2 5 6 9 11 11l4-3 6 6-4 5C17 33 5 21 3 8z"/><path d="M21 6a11 11 0 0 1 11 11M21 2a15 15 0 0 1 15 15M21 10a7 7 0 0 1 7 7"/></svg>Call</div>
  <div class="abs tile" style="left:158px;top:704px"><svg width="38" height="38" viewBox="0 0 38 38" fill="none" stroke="#222" stroke-width="1.4"><path d="M19 37V10M19 2l-4 6h8z M19 20L9 12M6 9l2 5 3-3z M19 20l10-8M32 9l-5 2 3 3z M19 26L7 22M19 26l12-4"/></svg>Direction</div>
  <div class="abs tile" style="left:281px;top:704px"><svg width="40" height="38" viewBox="0 0 40 38" fill="none" stroke="#222" stroke-width="1.4"><path d="M20 24s-7-8-7-13a7 7 0 0 1 14 0c0 5-7 13-7 13z"/><circle cx="20" cy="11" r="2.6"/><path d="M12 20l-9 3-1 13 12-3 12 3 12-3-1-13-8-3"/><path d="M8 31l5-4 5 3 6-4" stroke-dasharray="2 2"/></svg>Map</div>

  <div class="btn-red call-bar">
    <svg width="20" height="20" viewBox="0 0 20 20" fill="#fff"><path d="M4 1l4 4-2 3c1 3 4 6 7 7l3-2 4 4-3 3C8 19 1 12 1 4z"/></svg>CALL
  </div>
</section>

<!-- Check in -->
<section class="screen app-screen checkin">
  <svg class="abs back" width="14" height="22" viewBox="0 0 14 22" fill="none" stroke="#fff" stroke-width="2.6"><path d="M11 2L3 11l8 9"/></svg>
  <h2 class="abs serif app-head">Check In</h2>
  <svg class="abs more" width="6" height="22" viewBox="0 0 6 22" fill="#fff"><circle cx="3" cy="3" r="2.5"/><circle cx="3" cy="11" r="2.5"/><circle cx="3" cy="19" r="2.5"/></svg>
  <div class="abs sheet"></div>

  <svg class="abs cam" width="104" height="78" viewBox="0 0 104 78" fill="none" stroke="#141414" stroke-width="3"><path d="M3 16h28l8-12h24l8 12h30v59H3z"/><rect x="46" y="8" width="14" height="6"/><circle cx="52" cy="45" r="20"/><path d="M40 47a12 12 0 0 1 12-14"/><circle cx="90" cy="24" r="2" fill="#141414"/></svg>
  <p class="abs cam-text">Click on the Icon Above to<br>Take Your Picture</p>
  <h3 class="abs dates-head">UPCOMING COURT DATES</h3>

  <div class="abs court-row" style="top:418px"><span class="day">05</span><span class="dow">TUE</span><span class="court-name">Ravel Municipal</span><span class="court-time">Tue, Mar 05 2019 @ 12:00AM</span><span class="fee">$750.00</span></div>
  <div class="abs court-row shaded" style="top:492px"><span class="day">05</span><span class="dow">TUE</span><span class="court-name">Ravel Municipal</span><span class="court-time">Tue, Mar 05 2019 @ 12:00AM</span><span class="fee">$750.00</span></div>
  <div class="abs court-row" style="top:567px"><span class="day">05</span><span class="dow">TUE</span><span class="court-name">Ravel Municipal</span><span class="court-time">Tue, Mar 05 2019 @ 12:00AM</span><span class="fee">$750.00</span></div>
  <div class="abs court-row shaded" style="top:640px"><span class="day">05</span><span class="dow">TUE</span><span class="court-name">Ravel Municipal</span><span class="court-time">Tue, Mar 05 2019 @ 12:00AM</span><span class="fee">$750.00</span></div>
  <div class="abs court-row" style="top:716px"><span class="day">05</span><span class="dow">TUE</span><span class="court-name">Ravel Municipal</span><span class="court-time">Tue, Mar 05 2019 @ 12:00AM</span><span class="fee">$750.00</span></div>

  <div class="abs btn-cancel">CANCEL</div>
  <div class="btn-red btn-next">NEXT</div>
</section>

</body>
</html>
```